Halvern Cards

Technical services company
Networking, EAS, access control, project management and consultation

Clean, bold, modern design Using existing company logo for colors

Include Facebook and twitter links, QR bar code?

Industry/Entity Type

It Company

Contact Information for Business Card

Halvern Technical Services
"Steadfastly devoted to your progress"
860-555-0147 Main

Derek Voslund
Managing Partner / President
derek.voslund@halvern-ts.example
860-555-0183 Direct
www.halvern-ts.example

```html
<!DOCTYPE html>
<html lang="en">
<head>
<meta charset="utf-8">
<title>Halvern Technical Services – Business Cards</title>
<link href="https://fonts.googleapis.com/css2?family=Open+Sans:wght@400;700&display=swap" rel="stylesheet">
<style>
  :root {
    --bg: #e6e7e9;
    --card: #ffffff;
    --brand-blue: #2b3a9c;
    --brand-blue-mid: #1f6fd0;
    --brand-sky: #33a9ec;
    --brand-green: #3aa53a;
    --ink: #4a4a52;
    --ink-soft: #6a6a72;
  }
  * { box-sizing: border-box; margin: 0; padding: 0; }
  html, body { width: 1200px; height: 771px; overflow: hidden; }
  body {
    background: var(--bg);
    font-family: "Open Sans", Arial, sans-serif;
    position: relative;
  }
  .card {
    position: absolute;
    top: 231px;
    width: 540px;
    height: 309px;
    background: var(--card);
    box-shadow: 0 2px 10px rgba(0,0,0,0.12);
    overflow: hidden;
  }
  .card--back { left: 30px; }
  .card--front { left: 630px; }

  .brand {
    display: flex;
    align-items: center;
    gap: 14px;
  }
  .brand__dot {
    border-radius: 50%;
    background: radial-gradient(circle at 35% 35%, var(--brand-sky), var(--brand-blue) 75%);
    flex: none;
  }
  .brand__name {
    font-weight: 700;
    color: var(--brand-blue);
    line-height: 1.1;
  }

  .card--back .brand {
    position: absolute;
    left: 50px;
    top: 50%;
    transform: translateY(-50%);
  }
  .card--back .brand__dot { width: 96px; height: 96px; }
  .card--back .brand__name { font-size: 30px; }

  .card--front .brand {
    position: absolute;
    left: 28px;
    top: 24px;
  }
  .card--front .brand__dot { width: 50px; height: 50px; }
  .card--front .brand__name { font-size: 17px; }

  .address {
    position: absolute;
    left: 28px;
    top: 88px;
    font-size: 11px;
    color: var(--ink);
    line-height: 1.5;
  }

  .person {
    position: absolute;
    right: 28px;
    top: 30px;
    text-align: right;
  }
  .person__name {
    font-size: 17px;
    font-weight: 400;
    color: var(--brand-blue);
  }
  .person__title {
    font-size: 11px;
    color: var(--ink);
  }

  .swoosh {
    position: absolute;
    left: 0;
    bottom: 0;
    width: 540px;
    height: 309px;
  }

  .contacts {
    position: absolute;
    right: 28px;
    top: 150px;
    list-style: none;
    font-size: 10px;
    color: var(--ink-soft);
    text-align: right;
  }
  .contacts li {
    display: flex;
    justify-content: flex-end;
    align-items: center;
    gap: 6px;
    height: 17px;
  }
  .contacts svg { width: 10px; height: 10px; fill: var(--brand-blue); flex: none; }
</style>
</head>
<body>

  <section class="card card--back" aria-label="Business card back">
    <div class="brand">
      <span class="brand__dot"></span>
      <span class="brand__name">Halvern Technical Services</span>
    </div>
  </section>

  <section class="card card--front" aria-label="Business card front">
    <svg class="swoosh" viewBox="0 0 540 309" aria-hidden="true">
      <defs>
        <linearGradient id="swooshFill" x1="0" y1="0" x2="1" y2="0">
          <stop offset="0" stop-color="#2b3a9c"/>
          <stop offset="0.45" stop-color="#1f6fd0"/>
          <stop offset="0.7" stop-color="#33a9ec"/>
          <stop offset="1" stop-color="#2b3a9c"/>
        </linearGradient>
      </defs>
      <path d="M0 150 C 140 170, 330 230, 540 300 L 540 309 L 0 309 Z" fill="url(#swooshFill)"/>
      <path d="M0 132 C 150 150, 340 210, 540 288" fill="none" stroke="#3aa53a" stroke-width="5"/>
      <path d="M0 190 C 170 205, 350 255, 540 305" fill="none" stroke="#ffffff" stroke-opacity="0.35" stroke-width="2"/>
    </svg>

    <div class="brand">
      <span class="brand__dot"></span>
      <span class="brand__name">Halvern Technical Services</span>
    </div>

    <p class="address">41 Harbor Street, 6th Floor<br>Millbrook Road HTS</p>

    <div class="person">
      <p class="person__name">Derek Voslund</p>
      <p class="person__title">Managing Director</p>
    </div>

    <ul class="contacts">
      <li>860-555-0147
        <svg viewBox="0 0 10 10"><path d="M2 0.5 L3.8 2.6 L2.9 3.8 C3.6 5.2 4.8 6.4 6.2 7.1 L7.4 6.2 L9.5 8 L8.3 9.5 C4.3 9 1 5.7 0.5 1.7 Z"/></svg>
      </li>
      <li>860-555-0183
        <svg viewBox="0 0 10 10"><path d="M2.5 0 H7.5 V10 H2.5 Z M3.3 1 V8 H6.7 V1 Z"/></svg>
      </li>
      <li>derek.voslund@halvern-ts.example
        <svg viewBox="0 0 10 10"><path d="M0 2 H10 V8 H0 Z M1 3 L5 5.8 L9 3 V2.8 H1 Z" fill-rule="evenodd"/></svg>
      </li>
      <li>www.halvern-ts.example
        <svg viewBox="0 0 10 10"><circle cx="5" cy="5" r="4.5" fill="none" stroke="#2b3a9c" stroke-width="1"/><path d="M0.5 5 H9.5 M5 0.5 V9.5" stroke="#2b3a9c" stroke-width="0.8"/></svg>
      </li>
    </ul>
  </section>

</body>
</html>
```